TrueGrindz Complete Stationery - Logo already designed

I already have the logo designed see attached. I need have a full set of stationary and business card designed for printing. I have attached an example of what I mean.

Please feel free to be creative. Also you can use the X in the logo by its self if you think it will work.

My details:

Name: Corwin Lestak
Social media handles: @corwinlestak
W: corwinlestak.com
E: info@corwinlestak.com
​P: 08 7493 5286
PO Box 7382, Harwick Bay 6107
ABN 83 402 719 265

Target Market(s)

Anyone looking to be inspired.

Industry/Entity Type

Business

Font styles to use
Sans Serif

Colors
fbee3e
000000

Requirements
Must have
• My details:
• Name: Corwin Lestak
• Social media handles: @corwinlestak
• W: corwinlestak.com
• E: info@corwinlestak.com
• ​P: 08 7493 5286
• PO Box 7382, Harwick Bay 6107
• ABN 83 402 719 265
Nice to have
• Something a little different
Should not have
• must not look tacky.

```html
<!DOCTYPE html>
<html lang="en">
<head>
<meta charset="utf-8">
<title>TrueGrindz Letterhead</title>
<link rel="stylesheet" href="https://fonts.googleapis.com/css2?family=Source+Sans+3:wght@400;600;800&display=swap">
<style>
  :root {
    --backdrop: #9a9a9a;
    --paper: #ffffff;
    --ink: #111111;
    --accent: #f3b21c;
    --band: #0d0d0d;
  }
  * { margin: 0; padding: 0; box-sizing: border-box; }
  html, body {
    width: 1200px;
    height: 1200px;
    overflow: hidden;
    background: var(--backdrop);
    font-family: "Source Sans 3", Arial, sans-serif;
  }
  .letterhead {
    position: absolute;
    left: 210px;
    top: 48px;
    width: 780px;
    height: 1104px;
    background: var(--paper);
    box-shadow: 0 12px 40px rgba(0,0,0,0.25);
  }
  .brand-name {
    position: absolute;
    top: 56px;
    right: 60px;
    font-weight: 800;
    font-size: 46px;
    letter-spacing: -0.5px;
    color: var(--ink);
    line-height: 1;
  }
  .footer-details {
    position: absolute;
    left: 0;
    right: 0;
    bottom: 70px;
    text-align: center;
    font-size: 12px;
    color: var(--ink);
    line-height: 1.6;
  }
  .footer-details .label { color: var(--accent); font-weight: 600; }
  .social-row {
    display: flex;
    justify-content: center;
    align-items: center;
    gap: 6px;
    margin-top: 3px;
  }
  .social-square {
    width: 11px;
    height: 11px;
    background: var(--ink);
  }
  .footer-band {
    position: absolute;
    left: 0;
    right: 0;
    bottom: 0;
    height: 46px;
    background: var(--band);
  }
  .band-mark {
    position: absolute;
    right: 60px;
    top: 14px;
    width: 18px;
    height: 18px;
    background: var(--accent);
  }
</style>
</head>
<body>
  <main class="letterhead">
    <div class="brand-name">TrueGrindz</div>

    <footer class="footer-details">
      <div>PO Box 7382, Harwick Bay 6107</div>
      <div>
        <span class="label">P:</span> 08 7493 5286
        <span class="label">E:</span> info@corwinlestak.com
        <span class="label">W:</span> corwinlestak.com
        <span class="label">ABN:</span> 83 402 719 265
      </div>
      <div class="social-row">
        <span class="social-square"></span>
        <span>@corwinlestak</span>
      </div>
    </footer>

    <div class="footer-band">
      <span class="band-mark"></span>
    </div>
  </main>
</body>
</html>
```